Cedar Hall businesscard

We changed our name and logo, now we need new business cards.
3-4/72 Marlow Street Larkfield 2190
www.cedarhall-example.org.au
info@cedarhall-example.org.au
Lorna-Jean Whitcombe
Senior Pastor
ph: 02 95874210

```html
<!DOCTYPE html>
<html lang="en">
<head>
<meta charset="utf-8">
<title>Cedar Hall – Business Cards</title>
<link rel="stylesheet" href="https://fonts.googleapis.com/css2?family=Raleway:ital,wght@0,600;1,400&family=Titillium+Web:wght@400&display=swap">
<style>
  :root {
    --paper: #ffffff;
    --accent-orange: #cd6532;
    --accent-slate: #6f8797;
    --card-border: #7d8b98;
    --text-slate: #71889a;
    --text-grey: #5a5c5f;
    --text-light: #ffffff;
  }
  html, body {
    margin: 0;
    padding: 0;
    width: 1200px;
    height: 704px;
    overflow: hidden;
    background: var(--paper);
  }
  .canvas {
    position: relative;
    width: 1200px;
    height: 704px;
  }
  .card {
    position: absolute;
    box-sizing: border-box;
    border: 1.5px solid var(--card-border);
    background: var(--paper);
    overflow: hidden;
  }
  .name-band {
    color: var(--text-light);
    text-align: center;
    box-sizing: border-box;
  }
  .person-name {
    margin: 0;
    font-family: "Raleway", sans-serif;
    font-weight: 600;
    font-size: 24px;
    line-height: 1.28;
  }
  .person-role {
    margin: 0;
    font-family: "Raleway", sans-serif;
    font-style: italic;
    font-weight: 400;
    font-size: 20px;
  }
  .contact {
    font-family: "Titillium Web", sans-serif;
    font-weight: 400;
    margin: 0;
  }

  /* Wordmark: plain circle beside the name, one colour, one weight */
  .wordmark {
    position: absolute;
    display: flex;
    align-items: center;
    justify-content: center;
    gap: 8px;
    font-family: "Titillium Web", sans-serif;
    font-weight: 400;
    font-size: 20px;
    color: var(--text-slate);
    white-space: nowrap;
  }
  .wordmark-dot {
    width: 18px;
    height: 18px;
    border-radius: 50%;
    background: var(--text-slate);
    flex: none;
  }

  /* Landscape card */
  .card--landscape { left: 31px; top: 117px; width: 424px; height: 257px; }
  .card--landscape .name-band {
    background: var(--accent-orange);
    height: 83px;
    padding-top: 14px;
  }
  .card--landscape .person-role { margin-top: -2px; }
  .card--landscape .wordmark { left: 14px; top: 99px; width: 146px; height: 140px; }
  .card--landscape .contact {
    position: absolute;
    left: 182px;
    top: 101px;
    color: var(--text-slate);
    font-size: 17px;
    line-height: 25.5px;
  }
  .card--landscape .contact-gap { display: block; height: 9px; }

  /* Portrait cards */
  .card--portrait { width: 256px; height: 423px; }
  .card--orange { left: 557px; top: 116px; }
  .card--slate { left: 915px; top: 118px; }
  .card--portrait .wordmark { left: 0; right: 0; top: 0; height: 161px; }
  .card--portrait .name-band {
    position: absolute;
    left: 0; right: 0;
    top: 161px;
    height: 112px;
    padding-top: 7px;
  }
  .card--orange .name-band { background: var(--accent-orange); }
  .card--slate .name-band { background: var(--accent-slate); }
  .card--portrait .person-name { line-height: 31px; }
  .card--portrait .person-role { margin-top: 9px; }
  .card--portrait .contact {
    position: absolute;
    left: 0; right: 0;
    top: 281px;
    text-align: center;
    color: var(--text-grey);
    font-size: 17.5px;
    line-height: 26px;
  }
  .card--slate .contact { line-height: 27px; }
</style>
</head>
<body>
<main class="canvas">

  <!-- Landscape layout -->
  <article class="card card--landscape">
    <header class="name-band">
      <h1 class="person-name">Lorna-Jean Whitcombe</h1>
      <p class="person-role">Senior Pastor</p>
    </header>
    <div class="wordmark"><span class="wordmark-dot"></span>Cedar Hall</div>
    <p class="contact">
      ph: (02) 9587-4210<br>
      3-4/72 Marlow Street<br>
      Larkfield 2190<br>
      <span class="contact-gap"></span>
      www.cedarhall-example.org.au<br>
      info@cedarhall-example.org.au
    </p>
  </article>

  <!-- Portrait layout, orange -->
  <article class="card card--portrait card--orange">
    <div class="wordmark"><span class="wordmark-dot"></span>Cedar Hall</div>
    <header class="name-band">
      <h2 class="person-name">Lorna-Jean<br>Whitcombe</h2>
      <p class="person-role">Senior Pastor</p>
    </header>
    <p class="contact">
      ph: (02) 9587-4210<br>
      3-4/72 Marlow Street<br>
      Larkfield 2190<br>
      www.cedarhall-example.org.au<br>
      info@cedarhall-example.org.au
    </p>
  </article>

  <!-- Portrait layout, slate -->
  <article class="card card--portrait card--slate">
    <div class="wordmark"><span class="wordmark-dot"></span>Cedar Hall</div>
    <header class="name-band">
      <h2 class="person-name">Lorna-Jean<br>Whitcombe</h2>
      <p class="person-role">Senior Pastor</p>
    </header>
    <p class="contact">
      ph: (02) 9587-4210<br>
      3-4/72 Marlow Street<br>
      Larkfield 2190<br>
      www.cedarhall-example.org.au<br>
      info@cedarhall-example.org.au
    </p>
  </article>

</main>
</body>
</html>
```